Personality Workshop Template

I teach a workshop to business people that helps them identify and work with different personality types. We recently had our workbook redesigned and I want the power point to match. (This designer doesn't do power points.) I will upload both the workbook and the current class. I need a matching look that I can use for future classes. Each class is tailored to the client. I need 3-4 template slides that I can use interchangeably as I tailor the classes.

```html
<!DOCTYPE html>
<html lang="en">
<head>
<meta charset="UTF-8">
<title>Workshop Title Slide</title>
<link rel="stylesheet" href="https://fonts.googleapis.com/css2?family=Roboto+Condensed:wght@400;700&display=swap">
<style>
  :root {
    --blue-deep: #1f3f9c;
    --blue-photo-dark: #23409f;
    --blue-photo-light: #4a66c4;
    --green: #7ad61f;
    --white: #ffffff;
  }
  * { margin: 0; padding: 0; box-sizing: border-box; }
  html, body { width: 1200px; height: 900px; overflow: hidden; background: var(--blue-deep); }
  .slide {
    position: relative;
    width: 1200px;
    height: 900px;
    overflow: hidden;
    font-family: "Roboto Condensed", Arial, sans-serif;
    color: var(--white);
  }
  .hero-photo {
    position: absolute;
    inset: 0;
    background:
      radial-gradient(ellipse at 70% 35%, var(--blue-photo-light) 0%, transparent 60%),
      linear-gradient(135deg, var(--blue-photo-light) 0%, var(--blue-photo-dark) 70%);
  }
  .footer-band { position: absolute; left: 0; top: 0; width: 1200px; height: 900px; }
  .title-block { position: absolute; left: 55px; top: 500px; }
  .project-title {
    font-size: 64px;
    font-weight: 700;
    letter-spacing: 1px;
    line-height: 1;
    text-transform: uppercase;
  }
  .project-title .accent { color: var(--green); }
  .intro-lines { margin-top: 30px; font-size: 25px; line-height: 42px; font-weight: 400; }
  .workshop-name {
    position: absolute;
    left: 28px;
    top: 838px;
    font-size: 31px;
    font-weight: 700;
    letter-spacing: 0.5px;
  }
  .workshop-name .accent { color: var(--green); }
  .copyright {
    position: absolute;
    left: 592px;
    top: 840px;
    font-size: 18px;
    font-weight: 700;
  }
  .company-mark {
    position: absolute;
    left: 995px;
    top: 800px;
    display: flex;
    align-items: center;
    gap: 10px;
    font-size: 20px;
    font-weight: 700;
    line-height: 1.1;
    width: 180px;
  }
  .company-mark .dot { width: 14px; height: 14px; flex: none; background: var(--white); border-radius: 50%; }
</style>
</head>
<body>
  <main class="slide">
    <div class="hero-photo" role="img" aria-label="Blue-toned photo of a saxophone player and a singer in a top hat at a microphone"></div>

    <svg class="footer-band" viewBox="0 0 1200 900" aria-hidden="true">
      <path d="M0,780 C120,820 300,815 520,785 C760,752 1000,725 1200,735 L1200,900 L0,900 Z" fill="var(--blue-deep)"/>
      <path d="M0,780 C120,820 300,815 520,785 C760,752 1000,725 1200,735" fill="none" stroke="var(--green)" stroke-width="4"/>
    </svg>

    <section class="title-block">
      <h1 class="project-title">Project <span class="accent">Title Here</span></h1>
      <p class="intro-lines">
        Lorem ipsum dolor sit lorem ipsum dolor sit<br>
        Lorem ipsum dolor sit lorem<br>
        Lorem ipsum dolor sit lorem ipsum dolor sit.
      </p>
    </section>

    <div class="workshop-name">TEMPER<span class="accent">(AMENT)</span> TUNE</div>
    <div class="copyright">Copyright text here</div>
    <div class="company-mark"><span class="dot"></span><span>Tempo Business Consulting</span></div>
  </main>
</body>
</html>
```